Perfect — here’s the updated version of your description with **title #1** and the integration/booking functionality references removed, while still keeping the “motivation to book” idea in the design style:
---
**Luxury Property Website Design – Dominican Republic**
We are looking to create a professional and visually appealing **website design** for a premium property that we will be promoting as a short-term rental.
The property is located in an **exclusive area of the Dominican Republic** and offers a high-end experience for guests. Our goal is to create a website that highlights the **luxury, comfort, and exclusivity** of the property, while motivating visitors to **make a reservation inquiry**.
**Key Requirements:**
* A clean, modern, and elegant design that reflects the **premium nature** of the property.
* High-quality visual presentation of the **property’s best features** (rooms, amenities, location, views, nearby attractions).
* Easy-to-navigate structure
* Mobile-friendly and optimized for all screen sizes.
* Space for testimonials or guest reviews to build trust.
**Design Style We Like:**
* Elegant and sophisticated, with a touch of tropical luxury.
* Use of high-quality photography, subtle animations, and a warm color palette that reflects the Caribbean atmosphere.
* A premium feel, similar to boutique hotel or luxury villa rental websites.
**Deliverables:**
* Homepage design.
* Property detail page design (with gallery, amenities, and booking inquiry section).
Contact page or About Us page
* Photo Gallery
The final design should capture the essence of a **luxury getaway** and make visitors feel compelled to reserve their night.

```html
<!DOCTYPE html>
<html lang="en">
<head>
<meta charset="utf-8">
<title>Casa Marea – Luxury Villa</title>
<link rel="stylesheet" href="https://fonts.googleapis.com/css2?family=Poppins:wght@400;500;700;800&family=Roboto:wght@400;500;700&display=swap">
<style>
:root{
  --navy:#0b3a66;
  --orange:#f9a12e;
  --ink:#222;
  --muted:#8a8f96;
  --pale:#eef3f8;
  --white:#fff;
}
*{box-sizing:border-box;margin:0;padding:0}
html,body{width:1200px;height:3855px;overflow:hidden}
body{position:relative;font-family:Roboto,Arial,sans-serif;color:var(--ink);background:var(--white)}
.abs{position:absolute}
.heading{font-family:Poppins,Arial,sans-serif;font-size:40px;line-height:1;letter-spacing:.5px;text-transform:uppercase;white-space:nowrap}
.heading b{font-weight:800;color:var(--navy)}
.heading span{font-weight:400;color:var(--orange)}
.eyebrow{font-family:Roboto,sans-serif;font-weight:500;font-size:17px;color:var(--muted);text-transform:uppercase;letter-spacing:.3px}
.center{left:0;width:1200px;text-align:center}
.underline{width:44px;height:3px;background:var(--orange)}
.btn{background:var(--orange);color:#fff;font-weight:700;font-size:15px;text-transform:uppercase;display:flex;align-items:center;justify-content:center}

/* top bar */
.topbar{left:0;top:0;width:1200px;height:46px;background:var(--navy)}
.topbar .social{left:899px;top:0;width:301px;height:46px;background:var(--orange)}
.top-item{top:8px;display:flex;align-items:center;gap:12px;color:#fff;font-size:14px;font-weight:500}
.ic-circle{width:30px;height:30px;border-radius:50%;background:#fff;display:flex;align-items:center;justify-content:center}
.sq{top:0;width:36px;height:46px;display:flex;align-items:center;justify-content:center}
.sq i{display:block;width:11px;height:11px;border:2px solid #fff;border-radius:50%}

/* header */
.brand{display:flex;align-items:center;gap:12px;font-family:Poppins,sans-serif;font-size:30px;font-weight:700;color:var(--navy);letter-spacing:.5px;white-space:nowrap}
.brand-mark{width:18px;height:18px;background:var(--orange)}
.nav a{position:absolute;top:86px;font-family:Roboto,sans-serif;font-weight:700;font-size:15px;color:var(--navy);text-decoration:none;white-space:nowrap}
.nav a.active{color:var(--orange)}

/* hero */
.hero-title{top:273px;font-family:Poppins,sans-serif;font-weight:800;font-size:40px;line-height:53px;color:#fff;text-transform:uppercase;text-shadow:0 2px 6px rgba(0,0,0,.3)}
.hero-sub{top:387px;font-size:25px;color:#fff;text-shadow:0 1px 4px rgba(0,0,0,.35)}
.field{height:45px;background:#fff;border-radius:2px;font-size:14px;color:#333;display:flex;align-items:center;justify-content:space-between;padding:0 16px}
.dots{display:flex;gap:9px}
.dots i{width:13px;height:13px;border:2px solid #fff;border-radius:50%}
.dots i.on{background:#fff}

/* about */
.body-text{font-size:15.5px;line-height:26px;color:#333;text-align:justify}

/* features */
.card{background:#fff;box-shadow:0 4px 18px rgba(0,0,0,.1)}
.amen{list-style:none;font-size:16px;line-height:27.5px;color:#333}
.amen li{position:relative;padding-left:20px}
.amen li:before{content:"";position:absolute;left:0;top:12px;width:5px;height:5px;border-radius:50%;background:var(--orange)}

/* testimonials */
.tcard{top:2346px;width:305px;height:272px;background:#fff;padding:22px 22px 0}
.stars{color:var(--orange);font-size:15px;letter-spacing:2px}
.tcard p{margin-top:10px;font-size:13.5px;line-height:23px;color:#555;text-align:justify;height:116px}
.tcard hr{border:0;border-top:1px solid #e3e3e3;margin-top:4px}
.person{display:flex;align-items:center;gap:18px;margin-top:16px}
.avatar{width:55px;height:55px;border-radius:50%;background:linear-gradient(135deg,#c9c2b8,#8e8577)}
.person b{display:block;font-size:14px;color:var(--navy);font-weight:700}
.person small{font-size:12px;color:#777}

/* footer */
.f-title{font-family:Roboto,sans-serif;font-weight:700;font-size:17px;color:#fff;text-transform:uppercase}
.f-link{display:flex;align-items:center;gap:20px;color:#fff;font-size:14px;position:absolute}
.f-link i{width:13px;height:13px;border-radius:50%;background:var(--orange);display:block}
.f-info b{display:block;color:#fff;font-size:14px;font-weight:700}
.f-info span{display:block;color:#fff;font-size:12px;line-height:18px;margin-top:4px}
.round{width:34px;height:34px;border-radius:50%;border:1.5px solid #fff;display:flex;align-items:center;justify-content:center}
.round i{width:10px;height:10px;border-radius:50%;background:#fff;display:block}
.footer-brand{font-family:Poppins,sans-serif;font-weight:700;font-size:28px;line-height:38px;color:#fff;letter-spacing:.5px}
</style>
</head>
<body>

<!-- Top bar -->
<div class="abs topbar">
  <div class="abs top-item" style="left:111px">
    <span class="ic-circle"><svg width="14" height="14" viewBox="0 0 24 24"><path fill="#f9a12e" d="M6.6 10.8c1.4 2.8 3.8 5.1 6.6 6.6l2.2-2.2c.3-.3.7-.4 1-.2 1.1.4 2.3.6 3.6.6.6 0 1 .4 1 1V20c0 .6-.4 1-1 1C10.6 21 3 13.4 3 4c0-.6.4-1 1-1h3.5c.6 0 1 .4 1 1 0 1.3.2 2.5.6 3.6.1.3 0 .7-.2 1z"/></svg></span>
    +1.555.010.2040 <span style="margin-left:14px">|</span>
  </div>
  <div class="abs top-item" style="left:297px">
    <span class="ic-circle"><svg width="14" height="14" viewBox="0 0 24 24"><path fill="#f9a12e" d="M2 5h20v14H2z"/><path d="M2 5l10 8 10-8" stroke="#fff" stroke-width="2" fill="none"/></svg></span>
    hello@casamarea.example
  </div>
  <div class="abs social">
    <div class="abs sq" style="left:75px;background:#fff"><i style="border-color:var(--navy)"></i></div>
    <div class="abs sq" style="left:112px"><i></i></div>
    <div class="abs sq" style="left:151px"><i></i></div>
  </div>
</div>

<!-- Header -->
<div class="abs brand" style="left:111px;top:74px"><span class="brand-mark"></span>CASA MAREA</div>
<nav class="nav">
  <a class="active" style="left:613px">HOME</a>
  <a style="left:687px">ABOUT US</a>
  <a style="left:791px">PROPERTY</a>
  <a style="left:899px">GALLERY</a>
  <a style="left:996px">CONTACT US</a>
</nav>

<!-- Hero -->
<svg class="abs" style="left:0;top:136px" width="1200" height="642" viewBox="0 0 1200 642">
  <defs>
    <linearGradient id="heroGrad" x1="0" y1="0" x2="1" y2="1">
      <stop offset="0" stop-color="#a9b8c4"/>
      <stop offset=".4" stop-color="#5d7a72"/>
      <stop offset=".7" stop-color="#2f4a3a"/>
      <stop offset="1" stop-color="#1f3a44"/>
    </linearGradient>
  </defs>
  <polygon points="0,0 1200,0 1200,488 600,612 0,488" fill="url(#heroGrad)" role="img" aria-label="Photo of an infinity pool villa overlooking a tropical bay"/>
  <polygon points="0,488 600,612 1200,488 1200,508 600,642 0,512" fill="var(--orange)"/>
</svg>
<div class="abs center hero-title">Your private paradise in the<br>Dominican Republic</div>
<div class="abs center hero-sub">Luxury villa experience for unforgettable stays</div>
<div class="abs field" style="left:180px;top:452px;width:273px">Name</div>
<div class="abs field" style="left:464px;top:452px;width:274px">Phone</div>
<div class="abs field" style="left:747px;top:452px;width:273px">Email</div>
<div class="abs field" style="left:180px;top:507px;width:273px">location <svg width="10" height="6"><path d="M0 0h10L5 6z" fill="#333"/></svg></div>
<div class="abs field" style="left:464px;top:507px;width:274px">Date <svg width="12" height="12" viewBox="0 0 12 12"><rect x="1" y="2" width="10" height="9" fill="none" stroke="#555"/><path d="M1 5h10M3 0v3M9 0v3" stroke="#555"/></svg></div>
<div class="abs btn" style="left:747px;top:507px;width:273px;height:45px;border-radius:2px">Book your stay</div>
<div class="abs dots" style="left:558px;top:708px"><i></i><i class="on"></i><i></i><i></i></div>

<!-- About -->
<div class="abs" role="img" aria-label="Photo of a modern white villa with pool at dusk" style="left:111px;top:869px;width:462px;height:427px;background:linear-gradient(160deg,#8fb4d9,#e9e5dc 55%,#c7a77a)"></div>
<div class="abs" role="img" aria-label="Photo of a couple on a deck watching the sunset over the sea" style="left:367px;top:1122px;width:296px;height:227px;background:linear-gradient(180deg,#f0a35a,#e6b98a 45%,#5d6570);outline:6px solid #fff"></div>
<div class="abs eyebrow" style="left:726px;top:884px">Who we are</div>
<div class="abs heading" style="left:726px;top:911px"><b>About</b> <span>Us</span></div>
<div class="abs underline" style="left:693px;top:956px"></div>
<p class="abs body-text" style="left:726px;top:983px;width:362px">Lorem ipsum dolor sit amet, consectetur adipiscing elit, sed do eiusmod tempor incididunt ut labore et dolore magna aliqua. Ut enim ad minim veniam, quis nostrud exercitation ullamco laboris nisi ut aliquip ex ea commodo consequat. Duis aute irure dolor in reprehenderit in voluptate velit esse cillum dolore eu fugiat nulla pariatur.</p>
<p class="abs body-text" style="left:726px;top:1181px;width:362px">Lorem ipsum dolor sit amet, consectetur adipiscing elit, sed do eiusmod tempor incididunt ut labore et dolore magna aliquea.</p>
<div class="abs btn" style="left:726px;top:1288px;width:146px;height:49px">Learn more</div>

<!-- Features -->
<svg class="abs" style="left:0;top:1440px" width="1200" height="740" viewBox="0 0 1200 740">
  <polygon points="0,118 322,8 1200,26 1200,740 0,740" fill="var(--pale)"/>
  <polygon points="913,86 1200,26 1200,126" fill="var(--navy)"/>
</svg>
<div class="abs eyebrow center" style="top:1575px">Property amenities</div>
<div class="abs heading center" style="top:1601px"><b>Property</b> <span>Features</span></div>
<div class="abs underline" style="left:578px;top:1648px"></div>
<div class="abs" role="img" aria-label="Aerial photo of a white villa with pool and garden" style="left:111px;top:1683px;width:597px;height:428px;background:linear-gradient(135deg,#e8e9e6 30%,#59a3c9 55%,#6d8f4a 75%,#a7872e)"></div>
<div class="abs card" style="left:667px;top:1728px;width:421px;height:341px;padding:26px 40px">
  <div style="font-size:13px;color:#333;display:flex;align-items:center;gap:6px"><svg width="9" height="12" viewBox="0 0 9 12"><path d="M4.5 0A4.5 4.5 0 0 0 0 4.5C0 8 4.5 12 4.5 12S9 8 9 4.5A4.5 4.5 0 0 0 4.5 0z" fill="var(--orange)"/><circle cx="4.5" cy="4.5" r="1.6" fill="#fff"/></svg>United States</div>
  <div style="margin-top:14px;font-weight:700;font-size:17px;line-height:26px;color:var(--navy)">LOREM IPSUM DOLOR SIT AMET CONSEC TETUR ADIPISCING</div>
  <div style="margin-top:12px;font-size:13px;font-weight:700;color:#333">3 beds • 2 baths • 1,334 sqft</div>
  <ul class="amen" style="margin-top:10px">
    <li>Infinity Swimming Pool / Jacuzzi</li>
    <li>Home Theater / Entertainment Room</li>
    <li>Spa &amp; Sauna Facilities</li>
    <li>Game Room / Billiards</li>
  </ul>
  <div class="btn" style="margin-top:16px;width:158px;height:44px;font-size:14px">Book a inquiry</div>
</div>

<!-- Testimonials -->
<div class="abs" role="img" aria-label="Warm orange-tinted photo of a villa exterior" style="left:0;top:2180px;width:1200px;height:541px;background:linear-gradient(180deg,#f4a83b,#f7ad3e 50%,#f2a232)"></div>
<div class="abs center" style="top:2238px;font-weight:700;font-size:17px;color:#fff">TESTIMONIALS</div>
<div class="abs heading center" style="top:2264px"><b style="color:#fff">What our</b> <span style="color:#fff">Clients say</span></div>
<div class="abs underline" style="left:578px;top:2311px;background:#fff"></div>

<div class="abs tcard" style="left:111px">
  <div class="stars">★★★★★</div>
  <p>Lorem ipsum dolor sit amet, consectetur adipiscing elit, sed do eiusmod tempor incididunt ut labore et dolore magna aliqua. Ut enim ad minim veniam, quis nostrud exercitationea.</p>
  <hr>
  <div class="person"><div class="avatar" role="img" aria-label="Guest portrait"></div><div><b>MARCUS HALE</b><small>United States</small></div></div>
</div>
<div class="abs tcard" style="left:447px">
  <div class="stars">★★★★★</div>
  <p>Lorem ipsum dolor sit amet, consectetur adipiscing elit, sed do eiusmod tempor incididunt ut labore et dolore magna aliqua. Ut enim ad minim veniam, quis nostrud exercitationea.</p>
  <hr>
  <div class="person"><div class="avatar" role="img" aria-label="Guest portrait"></div><div><b>CLARA BENTON</b><small>United States</small></div></div>
</div>
<div class="abs tcard" style="left:783px">
  <div class="stars">★★★★★</div>
  <p>Lorem ipsum dolor sit amet, consectetur adipiscing elit, sed do eiusmod tempor incididunt ut labore et dolore magna aliqua. Ut enim ad minim veniam, quis nostrud exercitationea.</p>
  <hr>
  <div class="person"><div class="avatar" role="img" aria-label="Guest portrait"></div><div><b>MARCUS HALE</b><small>United States</small></div></div>
</div>
<div class="abs" style="left:571px;top:2656px;display:flex;gap:11px">
  <i style="width:6px;height:6px;border-radius:50%;background:rgba(255,255,255,.6)"></i>
  <i style="width:6px;height:6px;border-radius:50%;background:#fff"></i>
  <i style="width:6px;height:6px;border-radius:50%;background:rgba(255,255,255,.6)"></i>
  <i style="width:6px;height:6px;border-radius:50%;background:rgba(255,255,255,.6)"></i>
</div>

<!-- Gallery -->
<div class="abs eyebrow center" style="top:2801px">Gallery</div>
<div class="abs heading center" style="top:2826px"><b>Our</b> <span>Projects</span></div>
<div class="abs underline" style="left:578px;top:2873px"></div>

<div class="abs" role="img" aria-label="Photo of sun loungers by an infinity pool" style="left:111px;top:2902px;width:235px;height:192px;background:linear-gradient(180deg,#5fa6da,#e7e4de 55%,#c9b79b)"></div>
<div class="abs" role="img" aria-label="Photo of a glass villa facade with trees" style="left:111px;top:3106px;width:235px;height:233px;background:linear-gradient(160deg,#8fb8e0,#e4e2dd 45%,#6f9a4c)"></div>
<div class="abs" role="img" aria-label="Photo of a modern white villa with pool" style="left:359px;top:2902px;width:235px;height:257px;background:linear-gradient(180deg,#e8ecef,#b8bcc0 50%,#58b8c9)"></div>
<div class="abs" role="img" aria-label="Photo of a lit villa at dusk" style="left:359px;top:3173px;width:235px;height:166px;background:linear-gradient(180deg,#e9edf0,#8a6d52 60%,#4b6a3a)"></div>
<div class="abs" role="img" aria-label="Photo of a white townhouse with hedges" style="left:606px;top:2902px;width:236px;height:166px;background:linear-gradient(180deg,#d9e6ee,#efe9df 55%,#5b8a43)"></div>
<div class="abs" role="img" aria-label="Photo of a villa reflected in a pool" style="left:606px;top:3080px;width:236px;height:259px;background:linear-gradient(180deg,#e7e9ea,#cfd3d3 45%,#3b6b85)"></div>
<div class="abs" role="img" aria-label="Photo of a pool terrace with palm trees" style="left:854px;top:2902px;width:235px;height:257px;background:linear-gradient(180deg,#c5ddec,#5b7d53 40%,#3d8fc4)"></div>
<div class="abs" role="img" aria-label="Photo of an open-air dining pavilion" style="left:854px;top:3173px;width:235px;height:166px;background:linear-gradient(180deg,#a87852,#eae6df 45%,#d8d2c6)"></div>

<!-- Footer -->
<svg class="abs" style="left:0;top:3410px" width="1200" height="445" viewBox="0 0 1200 445">
  <polygon points="0,23 430,120 0,135" fill="var(--orange)"/>
  <polygon points="0,132 880,8 1200,76 1200,445 0,445" fill="var(--navy)"/>
</svg>
<div class="abs footer-brand" style="left:111px;top:3622px">CASA<br>MAREA</div>

<div class="abs f-title" style="left:344px;top:3552px">Quick links</div>
<div class="f-link" style="left:344px;top:3594px"><i></i>Home</div>
<div class="f-link" style="left:344px;top:3632px"><i></i>About Us</div>
<div class="f-link" style="left:344px;top:3669px"><i></i>Property</div>
<div class="f-link" style="left:344px;top:3707px"><i></i>Gallery</div>
<div class="f-link" style="left:344px;top:3745px"><i></i>Contact Us</div>

<div class="abs f-title" style="left:513px;top:3552px">Contact info</div>
<div class="abs f-info" style="left:551px;top:3594px;width:220px"><b>ADDRESS:</b><span>465, Lorum Ipsum Dolore Sed Amet, United States</span></div>
<div class="abs f-info" style="left:551px;top:3662px"><b>PHONE:</b><span>+1 (555) 010 2040</span></div>
<div class="abs f-info" style="left:551px;top:3727px"><b>EMAIL:</b><span>info@casamarea.example</span></div>
<svg class="abs" style="left:513px;top:3596px" width="11" height="14" viewBox="0 0 9 12"><path d="M4.5 0A4.5 4.5 0 0 0 0 4.5C0 8 4.5 12 4.5 12S9 8 9 4.5A4.5 4.5 0 0 0 4.5 0z" fill="var(--orange)"/><circle cx="4.5" cy="4.5" r="1.6" fill="var(--navy)"/></svg>
<svg class="abs" style="left:512px;top:3664px" width="13" height="13" viewBox="0 0 24 24"><path fill="var(--orange)" d="M6.6 10.8c1.4 2.8 3.8 5.1 6.6 6.6l2.2-2.2c.3-.3.7-.4 1-.2 1.1.4 2.3.6 3.6.6.6 0 1 .4 1 1V20c0 .6-.4 1-1 1C10.6 21 3 13.4 3 4c0-.6.4-1 1-1h3.5c.6 0 1 .4 1 1 0 1.3.2 2.5.6 3.6.1.3 0 .7-.2 1z"/></svg>
<svg class="abs" style="left:512px;top:3731px" width="15" height="11" viewBox="0 0 15 11"><rect width="15" height="11" fill="var(--orange)"/><path d="M0 0l7.5 6L15 0" stroke="var(--navy)" fill="none"/></svg>

<div class="abs f-title" style="left:805px;top:3552px">Join newsletter</div>
<div class="abs" style="left:805px;top:3596px;width:283px;height:47px;background:#fff;display:flex;align-items:center;padding:3px">
  <span style="flex:1;padding-left:14px;font-size:13px;color:#555">Email Address</span>
  <span class="btn" style="width:104px;height:39px;font-size:13px">Join now</span>
</div>
<div class="abs" style="left:806px;top:3668px;display:flex;gap:8px">
  <div class="round" style="background:var(--orange);border-color:var(--orange)"><i></i></div>
  <div class="round"><i></i></div>
  <div class="round"><i></i></div>
</div>

<div class="abs" style="left:111px;top:3788px;width:978px;height:1px;background:rgba(255,255,255,.25)"></div>
<div class="abs center" style="top:3815px;font-size:13px;color:#fff">© 2025 <b>CASA MAREA</b> &nbsp;| &nbsp;All Rights Reserved</div>

<div class="abs" style="left:1115px;top:3745px;width:44px;height:44px;border-radius:50%;background:#fff;display:flex;align-items:center;justify-content:center;box-shadow:0 2px 8px rgba(0,0,0,.25)">
  <svg width="22" height="20" viewBox="0 0 22 20"><path d="M2 2h13v9H7l-4 3v-3H2z" fill="var(--orange)"/><path d="M17 6h3v9h-1v3l-4-3H8v-2h9z" fill="var(--orange)" opacity=".7"/></svg>
</div>

</body>
</html>
```